Capability statement. I’ll send through what I put into GPT. Once layout is sorted I can send through more images

Target Market(s)

Tier 1 and 2 contractors

Industry/Entity Type

Civil construction

Colors
00AB8E
00BBA5
67D7C9
C6EFE9
E9F9F6

Requirements
Must have
• Black backgrounds and Matt charcoal/aqua colour scheme

```html
<!DOCTYPE html>
<html lang="en">
<head>
<meta charset="UTF-8">
<title>Karra Civil Group – Capability Statement</title>
<link href="https://fonts.googleapis.com/css2?family=Archivo:wght@800;900&family=Inter:wght@400;500;600;700&display=swap" rel="stylesheet">
<style>
:root{
  --charcoal:#1d1d1d;
  --charcoal-2:#232323;
  --aqua-deep:#00AB8E;
  --aqua:#00BBA5;
  --aqua-light:#67D7C9;
  --aqua-pale:#C6EFE9;
  --aqua-mist:#E9F9F6;
  --white:#ffffff;
  --ink:#1a1a1a;
}
*{margin:0;padding:0;box-sizing:border-box}
html,body{width:848px;height:1200px;overflow:hidden;background:#fff}
.sheet{position:relative;width:848px;height:1200px;overflow:hidden;font-family:"Inter",Arial,sans-serif;color:var(--white)}
.hero{position:absolute;left:0;top:0;width:848px;height:496px;background:var(--charcoal)}
.services{position:absolute;left:0;top:634px;width:848px;height:479px;background:var(--charcoal-2)}
.art{position:absolute;left:0;top:0}
.brand{position:absolute;left:42px;top:44px;font-weight:700;color:var(--white);line-height:1}
.brand-name{display:block;font-size:64px;letter-spacing:1px}
.brand-sub{display:block;font-size:20px;letter-spacing:9px;margin-top:8px}
.title{position:absolute;left:43px;top:210px;font-family:"Archivo",Arial,sans-serif;font-weight:900;font-size:51px;line-height:55px;letter-spacing:-1px}
.title .accent{color:var(--aqua-light)}
.tagline{position:absolute;left:43px;top:343px;font-size:21px;line-height:28px;font-weight:400}
.region{position:absolute;left:43px;top:419px;display:flex;align-items:center;gap:13px;font-size:23px}
.region-map{width:58px;height:48px;border-radius:4px;background:var(--aqua-deep);opacity:.35}
.values{position:absolute;left:0;top:496px;width:848px;height:138px;background:var(--white);display:flex;color:var(--ink)}
.value{display:flex;flex-direction:column;align-items:center;justify-content:center;gap:14px;font-size:17px;letter-spacing:.3px;border-right:1px solid #ddd;margin:16px 0}
.value:last-child{border-right:none}
.value svg{height:58px}
.services-title{position:absolute;left:43px;top:677px;font-family:"Archivo",Arial,sans-serif;font-weight:800;font-size:23px;letter-spacing:-.5px}
.services-title span{color:var(--aqua-light)}
.service-list{position:absolute;left:45px;top:734px;list-style:none}
.service{display:flex;align-items:center;height:67px;font-size:20px;letter-spacing:.4px}
.service svg{width:62px;height:70px;margin-right:25px;flex:none}
.footer{position:absolute;left:0;top:1113px;width:848px;height:87px;background:linear-gradient(90deg,var(--aqua-light),var(--aqua) 55%,var(--aqua-deep));display:flex;align-items:center;font-size:14px;font-weight:600}
.footer-brand{width:125px;padding-left:44px;line-height:17px;font-size:14px;font-weight:600}
.footer-cell{display:flex;flex-direction:column;justify-content:center;gap:10px;height:52px;border-left:1px solid rgba(255,255,255,.35);padding-left:29px}
.footer-row{display:flex;align-items:center;gap:8px}
.footer-row svg{width:20px;height:20px;flex:none}
</style>
</head>
<body>
<div class="sheet">
  <section class="hero">
    <svg class="art" width="848" height="496" viewBox="0 0 848 496">
      <defs>
        <linearGradient id="siteTop" x1="0" y1="0" x2="0" y2="1">
          <stop offset="0" stop-color="#e6ecef"/>
          <stop offset=".55" stop-color="#7ea9a0"/>
          <stop offset="1" stop-color="#c7a984"/>
        </linearGradient>
      </defs>
      <polygon points="399,0 413,0 494,496 480,496" fill="#00BBA5"/>
      <polygon points="413,0 848,0 848,496 494,496" fill="url(#siteTop)" role="img" aria-label="Photo: aqua excavator laying pipe in a drainage trench on a civil site"/>
    </svg>
    <div class="brand"><span class="brand-name">KARRA</span><span class="brand-sub">CIVIL GROUP</span></div>
    <h1 class="title">CAPABILITY<br><span class="accent">STATEMENT</span></h1>
    <p class="tagline">Delivering Civil Infrastructure,<br>Earthworks &amp; Drainage Solutions</p>
    <div class="region"><div class="region-map" role="img" aria-label="Outline map of New South Wales"></div>Across NSW</div>
  </section>

  <section class="values">
    <div class="value" style="width:243px">
      <svg viewBox="0 0 100 50" fill="#1a1a1a"><circle cx="16" cy="14" r="6"/><circle cx="84" cy="14" r="6"/><path d="M2 46a14 14 0 0 1 26-8v8z"/><path d="M98 46a14 14 0 0 0-26-8v8z"/><circle cx="50" cy="10" r="8" fill="none" stroke="#1a1a1a" stroke-width="3.5"/><path d="M30 46a20 18 0 0 1 40 0z" fill="none" stroke="#1a1a1a" stroke-width="3.5"/></svg>
      EXPERIENCED TEAM</div>
    <div class="value" style="width:181px">
      <svg viewBox="0 0 100 50" fill="none" stroke="#1a1a1a" stroke-width="3.5" stroke-linejoin="round"><path d="M3 40V20h22v20M25 40h30V2h18v38h-8M55 20h18"/><path d="M80 40l8-20 10 20z"/><circle cx="12" cy="42" r="7"/><circle cx="64" cy="42" r="7"/></svg>
      MODERN FLEET</div>
    <div class="value" style="width:202px">
      <svg viewBox="0 0 60 60" fill="none" stroke="#1a1a1a" stroke-width="3.5"><circle cx="30" cy="30" r="27"/><circle cx="30" cy="30" r="15"/><circle cx="30" cy="30" r="2.5" fill="#1a1a1a"/></svg>
      SAFETY FOCUSED</div>
    <div class="value" style="width:222px">
      <svg viewBox="0 0 50 60" fill="none" stroke="#1a1a1a" stroke-width="3.5" stroke-linejoin="round"><path d="M25 3l21 8v20c0 14-10 22-21 26C14 53 4 45 4 31V11z"/><path d="M15 30l7 7 13-14"/></svg>
      PROVEN DELIVERY</div>
  </section>

  <section class="services">
    <svg class="art" width="848" height="479" viewBox="0 0 848 479">
      <defs>
        <linearGradient id="siteBottom" x1="0" y1="0" x2="1" y2="1">
          <stop offset="0" stop-color="#9a8a76"/>
          <stop offset=".5" stop-color="#a88a68"/>
          <stop offset="1" stop-color="#7d6a55"/>
        </linearGradient>
      </defs>
      <polygon points="483,0 497,0 398,479 384,479" fill="#00BBA5"/>
      <polygon points="497,0 848,0 848,479 398,479" fill="url(#siteBottom)" role="img" aria-label="Photo: excavator loading an articulated dump truck on an earthworks site"/>
    </svg>
  </section>
  <h2 class="services-title">Our <span>Services</span></h2>
  <ul class="service-list">
    <li class="service"><svg viewBox="0 0 62 70" fill="none" stroke="#00AB8E" stroke-width="1.5"><polygon points="31,1 61,18 61,52 31,69 1,52 1,18"/><path d="M18 46h26v-6H18zM22 40l6-12 8 4 4 8"/></svg>BULK EARTHWORKS</li>
    <li class="service"><svg viewBox="0 0 62 70" fill="none" stroke="#00AB8E" stroke-width="1.5"><polygon points="31,1 61,18 61,52 31,69 1,52 1,18"/><path d="M17 44h22M20 44v-8h14v8M34 36l8-10 4 6"/><circle cx="22" cy="47" r="2"/><circle cx="34" cy="47" r="2"/></svg>DETAILED EXCAVATION</li>
    <li class="service"><svg viewBox="0 0 62 70" fill="none" stroke="#00AB8E" stroke-width="1.5"><polygon points="31,1 61,18 61,52 31,69 1,52 1,18"/><path d="M18 46V24h8v22M30 40h14M18 50c4-2 6 2 10 0s6 2 10 0 6 2 8 0"/></svg>DRAINAGE</li>
    <li class="service"><svg viewBox="0 0 62 70" fill="none" stroke="#00AB8E" stroke-width="1.5"><polygon points="31,1 61,18 61,52 31,69 1,52 1,18"/><path d="M20 50c6-10 14-18 10-28M40 50c-4-10 4-18 0-28"/><path d="M30 46v-3M31 38v-3M32 30v-3"/></svg>ROADWORKS</li>
    <li class="service"><svg viewBox="0 0 62 70" fill="none" stroke="#00AB8E" stroke-width="1.5"><polygon points="31,1 61,18 61,52 31,69 1,52 1,18"/><path d="M18 48V30h26v18zM22 30v-6h6v6M36 30V22h6v8M22 36h4M30 36h4M38 36h3M22 42h4M30 42h4M38 42h3"/></svg>PLANT HIRE</li>
  </ul>

  <footer class="footer">
    <div class="footer-brand">KARRA<br>CIVIL<br>GROUP</div>
    <div class="footer-cell" style="width:269px">
      <div class="footer-row"><svg viewBox="0 0 24 24" fill="none" stroke="#fff" stroke-width="1.6"><circle cx="12" cy="12" r="10"/><path d="M2 12h20M12 2c3 3 4 6 4 10s-1 7-4 10c-3-3-4-6-4-10s1-7 4-10z"/></svg>www.karracivilgroup.com.au</div>
    </div>
    <div class="footer-cell" style="width:266px">
      <div class="footer-row"><svg viewBox="0 0 24 24" fill="none" stroke="#fff" stroke-width="1.6" stroke-linejoin="round"><path d="M5 2h4l2 5-3 2a12 12 0 0 0 7 7l2-3 5 2v4a2 2 0 0 1-2 2A19 19 0 0 1 3 4a2 2 0 0 1 2-2z"/></svg>0412 555 019</div>
      <div class="footer-row"><svg viewBox="0 0 24 24" fill="none" stroke="#fff" stroke-width="1.6"><rect x="2" y="5" width="20" height="14" rx="1"/><path d="M2 6l10 7 10-7"/></svg>info@karracivilgroup.com.au</div>
    </div>
    <div class="footer-cell" style="width:188px">
      <div class="footer-row"><svg viewBox="0 0 24 24" fill="none" stroke="#fff" stroke-width="1.6"><path d="M12 22s-7-7-7-12a7 7 0 0 1 14 0c0 5-7 12-7 12z"/><circle cx="12" cy="10" r="2.5"/></svg>sydney, NSW</div>
    </div>
  </footer>
</div>
</body>
</html>
```